都内でエステサロンを運営されている
美容家さんの電子書籍を出版しますので、
表紙デザイン作成をお願いいたします。

ーーーーーーーーーーー
■本のタイトル
月灯集

【サブタイトル】
朝の散歩で心を整える本

<著者>沙耶(さや)

ーーーーーーーーーー

納品は、2,560 x 1,600 ピクセルのJPEGと
元データをお願い致したく。

著者プロフィール
美容家、エステティシャン

サロンのイメージカラーはピンク、白ですが
表紙デザインに色のこだわりはありません。

ーーーー

■デザイン要望

優しさ,明るさ、清潔感と品格、プロフェッショナル感があるものをお願いします。

【コンセプト】
美容ジプシー、悩める女性たちに(男性も歓迎)贈りたい
優しく楽しい小さなご褒美タイムとその作法(洗顔やお肌のお手入れに関するメソッド)を提供する

肌質はみんなそれぞれちがいますが、本当に幸せな自分磨きは毎日のスキンケア一択。その極意を惜しみなく提供。

添付に表紙イメージの参考を挙げましたが
デザイナー様のセンスにお任せします。

ーーーーーーーーーー

※その他イラストや写真等素材を使用される場合には、商用利用可の素材をお願いします。
(Pavrelにて販売予定のため)

デザインを考えるのに必要な情報などありましたら、お答えしますので、ご遠慮なくお問い合わせ下さい。

納期は予告なく短縮する場合がございます。
よろしくお願い申し上げます。

著者様のご希望優先で決定させていただきました。

美容の道を極めた想いと、透明感、躍動感、生き生きとした理想の美人像を彷彿とさせる素敵な表紙ということで、選定させていただきます。

この度は、当コンペにご提案を頂き誠にありがとうございます。
リピートのデザイナー様もいらして、どれも素晴らしく貴重なお時間と労力を割いてくださって
本当にありがとうございました。心より感謝申し上げます。

今回選定できなかった方々の作品も大切に拝見し、個別に依頼できそうな案件などありましたらご紹介させていただきます。みなさまのご活躍祈念しております。

これからも大切に作品を制作してまいります。
どうぞまたコンペ開催の際にはご縁をいただけましたら幸いです。

本当にどうもありがとうございました。

```html
<!DOCTYPE html>
<html lang="ja">
<head>
<meta charset="UTF-8">
<title>月灯集 表紙</title>
<link rel="stylesheet" href="https://fonts.googleapis.com/css2?family=M+PLUS+Rounded+1c:wght@500;700;800&display=swap">
<style>
  :root {
    --cover-pink: #d65c82;
    --navy: #1f3354;
    --white: #ffffff;
    --title-box: #f4f4f6;
    --art-light: #e89ab3;
    --art-mid: #f3c9d5;
  }
  * { margin: 0; padding: 0; box-sizing: border-box; }
  html, body { width: 750px; height: 1200px; overflow: hidden; background: var(--cover-pink); }
  .cover {
    position: relative;
    width: 750px; height: 1200px;
    background: var(--cover-pink);
    font-family: "M PLUS Rounded 1c", sans-serif;
    overflow: hidden;
  }
  .title-box {
    position: absolute; left: 62px; top: 45px;
    width: 626px; height: 160px;
    background: var(--title-box);
    border-radius: 30px;
    display: flex; align-items: center; justify-content: center;
  }
  .title {
    color: var(--navy);
    font-size: 128px; font-weight: 800; letter-spacing: 6px; line-height: 1;
  }
  .author-role {
    position: absolute; left: 90px; top: 212px;
    color: var(--white); font-size: 21px; font-weight: 700;
  }
  .author-name {
    position: absolute; left: 90px; top: 244px;
    color: var(--white); font-size: 30px; font-weight: 700;
  }
  .illustration {
    position: absolute; left: 180px; top: 290px;
    width: 410px; height: 640px;
  }
  .vertical {
    position: absolute;
    display: flex; flex-direction: column; align-items: center;
    color: var(--navy); font-weight: 800;
    z-index: 2;
  }
  .vertical span {
    display: block; text-align: center; line-height: 1;
  }
  .vertical .rotate { transform: rotate(90deg); }
  .tagline { left: 104px; top: 385px; width: 54px; font-size: 44px; }
  .tagline span { height: 53px; }
  .subtitle { left: 636px; top: 262px; width: 76px; font-size: 60px; }
  .subtitle span { height: 66px; }
  .subtitle .on-band { color: var(--white); }
  .band {
    position: absolute; left: 0; top: 925px;
    width: 750px; height: 275px;
    background: var(--navy);
    color: var(--white);
    padding: 50px 0 0 100px;
    z-index: 1;
  }
  .band-line {
    font-size: 38px; font-weight: 800; line-height: 1; letter-spacing: 1px;
    margin-bottom: 34px;
  }
  .band-note {
    position: absolute; left: 0; right: 0; bottom: 24px;
    text-align: center; font-size: 23px; font-weight: 500;
  }
</style>
</head>
<body>
  <main class="cover">
    <div class="title-box"><h1 class="title">月灯集</h1></div>
    <p class="author-role">美容家 エステティシャン</p>
    <p class="author-name">沙耶(さや)</p>

    <svg class="illustration" role="img" aria-label="口紅を塗る女性のイラストと時計、きらめき" viewBox="0 0 410 640">
      <defs>
        <linearGradient id="artTone" x1="0" y1="0" x2="0" y2="1">
          <stop offset="0" stop-color="#f3c9d5"/>
          <stop offset="1" stop-color="#e89ab3"/>
        </linearGradient>
      </defs>
      <rect x="0" y="0" width="410" height="640" rx="40" fill="url(#artTone)"/>
    </svg>

    <p class="vertical tagline" aria-label="美容ジプシーも必見">
      <span>美</span><span>容</span><span>ジ</span><span>プ</span><span>シ</span><span class="rotate">ー</span><span>も</span><span>必</span><span>見</span>
    </p>

    <section class="band">
      <p class="band-line">悩める人たちに贈る</p>
      <p class="band-line">美の極意を惜しみなく提供</p>
      <p class="band-note">優しく楽しい小さなご褒美タイムとその作法をお教えします</p>
    </section>

    <h2 class="vertical subtitle" aria-label="朝の散歩で心を整える本">
      <span>朝</span><span>の</span><span>散</span><span>歩</span><span>で</span><span>心</span><span>を</span><span>整</span><span>え</span><span>る</span><span class="on-band">本</span>
    </h2>
  </main>
</body>
</html>
```